eBook book cover for erotic novel set in Singapore (yes really!)

Hello - here’s a bit of background on my book, along with some thoughts on the cover. I hope this helps; am happy to answer any questions and provide further example chapters if that would help you get a better idea of what it’s all about (some extracts are attached to this brief).

1. "Under Quiet Lanterns" - synopsis
“I'm curious—and tempted. Oh dear!” is Bea’s reply to an advert posted on the internet and she enters into a relationship unlike any other she has experienced before—one that stimulates, frustrates, consumes and ultimately, delights, her.

Owen a successful banker living in Singapore has placed an online invitation for “irregular intimacy” with a “sexy, well-dressed lover with stimulating kinks”. Bea’s feeling dulled by her demanding job and the undemanding social rituals of her life in Singapore: she’s attracted to Owen’s slightly jaded urbanity and quirky ways. He finds her plain-speaking exuberance a refreshing contrast to his own more conservative nature.

After a sparky, and at times, spiky, email exchange they meet at a rooftop bar in Singapore’s Chinatown. Over cocktails they agree the seven rules of their relationship (the first one—“No questions about work or personal lives”). Despite this formality, the sexual attraction between them is intense—as is the sex when they first manage to schedule it. Over subsequent weeks they craft a list of sexual experiences they intend to enjoy together. Once they’ve completed ‘The List’ (on an Excel spreadsheet) they’ll part. That’s the intention anyway.

As their relationship develops they both can’t help applying their controlling corporate selves to their secret life. Apart from the proposed experiences on the agreed list, each of them sometimes introduces new things to surprise the other. Under Quiet Lanterns is set mainly in Singapore—where the exotic sights, sounds and tastes provide a sensual backdrop to the increasingly intense affair.

The novel is about two people who believe they can manage their relationship in the same way they organise everything else in their lives—with closely calibrated calendar entries, tightly planned sexual liaisons and multiple lists. They relish the contrasts between their demanding jobs (the frequent travel, late night conference calls and always-on Quillphones) and indulging their imaginations with someone they trust. Bea begins to appreciate just what being “sex fit” entails. The sex scenes are explicit (“Sex where she did things she couldn’t tell her sisters about”) and driven in part by their competitive natures.

However, it gradually becomes clear that it is becoming harder for them to contain their relationship to just sex, no matter how delightful. They had both originally committed to a ‘no strings attached’ affair but they struggle with their growing feelings for each other. Owen initially drives the relationship but increasingly becomes out of his depth whilst Bea gains confidence. The novel ends with over half The List still to be completed—will they be able to keep to the rules, and more importantly, maintain the expected emotional distance they’ve both agreed to?

2. Cover thoughts
I’d like to avoid the typical cliched image of say, a silk tie and handcuffs, that one often sees on book covers of this genre. A reference to Singapore/Asia would be good of course (an orchid too obvious?), and naturally being an ebook, the cover needs to be simple and striking. I have a second book planned, and half written, and possibly a third. A design that thus lends itself to being adapted slightly so as to support a trilogy would be particularly useful.

3. Author's name
Gus Palmer

Thanks
Gus

Women 25-45

Serif
Decorative
Script

85cae6
3176b5

• A reference to Asia/Singapore
• A sense of the unknown, reference to Asia/Singapore, a hint of sex attraction, reference to corporate life.
• Just had a thought that a single stiletto shoe (on a carpet, wooden floorboards?) might be interesting.
• Be overly explicit sexually - have the usual cliche of a scantily clad woman for example

```html
<!DOCTYPE html>
<html lang="en">
<head>
<meta charset="utf-8">
<title>Under Quiet Lanterns – Cover Wrap</title>
<link rel="stylesheet" href="https://fonts.googleapis.com/css2?family=Josefin+Sans:wght@300;400&family=Questrial&display=swap">
<style>
  :root {
    --page-bg: #2a2d3d;
    --title-blue: #3a8fd0;
    --title-light: #6fb8e8;
    --text-navy: #3b4a86;
    --lavender: #b9b3e6;
    --sky: #a9cdef;
    --pale: #e6ecfb;
    --pink: #ef8fbf;
    --pink-deep: #e0619f;
    --pink-soft: #f6c6de;
    --shoe-pink: #d9479a;
  }
  * { margin: 0; padding: 0; box-sizing: border-box; }
  html, body { width: 1200px; height: 835px; overflow: hidden; }
  body {
    background: var(--page-bg);
    display: flex;
    align-items: center;
    justify-content: center;
  }
  .cover-wrap {
    display: flex;
    height: 700px;
    box-shadow: 0 20px 50px rgba(0,0,0,0.45);
  }
  .back-cover {
    width: 400px;
    background: linear-gradient(170deg, var(--lavender) 0%, var(--pale) 45%, var(--sky) 75%, var(--pink-soft) 100%);
    padding: 110px 36px 0;
    font-family: "Questrial", sans-serif;
    color: var(--text-navy);
    font-size: 14.5px;
    line-height: 1.72;
    text-align: center;
  }
  .back-cover p + p { margin-top: 22px; }
  .spine {
    width: 72px;
    background: linear-gradient(180deg, var(--pale) 0%, var(--sky) 55%, var(--pink-soft) 100%);
    display: flex;
    align-items: center;
    justify-content: center;
    border-left: 1px solid rgba(255,255,255,0.5);
    border-right: 1px solid rgba(255,255,255,0.5);
  }
  .spine-title {
    writing-mode: vertical-rl;
    font-family: "Josefin Sans", sans-serif;
    font-weight: 300;
    font-size: 38px;
    color: var(--title-blue);
    letter-spacing: 1px;
    white-space: nowrap;
  }
  .front-cover {
    position: relative;
    width: 400px;
    background: linear-gradient(180deg, #f4d7ec 0%, var(--sky) 22%, var(--pale) 38%, var(--pink-soft) 55%, var(--pink) 80%, var(--pink-deep) 100%);
    overflow: hidden;
  }
  .front-title {
    position: absolute;
    top: 18px;
    left: 0;
    right: 0;
    text-align: center;
    font-family: "Josefin Sans", sans-serif;
    font-weight: 300;
    font-size: 80px;
    line-height: 1.02;
    color: var(--title-blue);
    background: linear-gradient(180deg, var(--title-blue), var(--title-light));
    -webkit-background-clip: text;
    background-clip: text;
    -webkit-text-fill-color: transparent;
  }
  .front-title span { display: block; }
  .shoe-art {
    position: absolute;
    left: 30px;
    top: 330px;
    width: 330px;
    height: 260px;
  }
  .author-name {
    position: absolute;
    bottom: 28px;
    left: 0;
    right: 0;
    text-align: center;
    font-family: "Josefin Sans", sans-serif;
    font-weight: 400;
    font-size: 30px;
    letter-spacing: 3px;
    color: var(--title-blue);
  }
</style>
</head>
<body>
  <main class="cover-wrap">
    <section class="back-cover">
      <p>Books may also refer to works of literature, or a main division of such a work. In library and information science, a book is called a monograph, to distinguish it from serial periodicals such as magazines, journals or newspapers. The body of all written works including books is literature. In novels and sometimes other types of books (for example, biographies), a book may be divided into several large sections, also called books (Book 1, Book 2, Book 3, and so on). An avid reader of books is a bibliophile or colloquially, bookworm.</p>
      <p>A shop where books are bought and sold is a bookshop or bookstore. Books can also be borrowed from libraries. Northwind Index has estimated that as of 2010, approximately 130,000,000 unique titles had been published</p>
    </section>
    <section class="spine">
      <h2 class="spine-title">Under Quiet Lanterns</h2>
    </section>
    <section class="front-cover">
      <h1 class="front-title"><span>Under</span><span>Quiet</span><span>Lanterns</span></h1>
      <svg class="shoe-art" viewBox="0 0 330 260" role="img" aria-label="Photograph of a single pink stiletto shoe resting on white feathers">
        <defs>
          <radialGradient id="shoe-glow" cx="50%" cy="55%" r="55%">
            <stop offset="0%" stop-color="#d9479a" stop-opacity="0.75"/>
            <stop offset="60%" stop-color="#ef8fbf" stop-opacity="0.45"/>
            <stop offset="100%" stop-color="#f6c6de" stop-opacity="0"/>
          </radialGradient>
        </defs>
        <rect width="330" height="260" fill="url(#shoe-glow)"/>
      </svg>
      <p class="author-name">GUS PALMER</p>
    </section>
  </main>
</body>
</html>
```